Accounting Firm

We are a two partner accounting firm. our business name is BELLWOOD & TRASK. We are accountants and business consultants.

We need a stationery design for our letterhead, with compliments slip, business card and envelope.

We'd like clean, professional look. I'm 39 years old and my partner is 60+, so we'd like modern yet elegant design. Dark Navy Blue as a primary colour is preferred.

Thank you.
Updates

Hi Guys

No logo.

Thanks

Industry/Entity Type

Accounting

Requirements
Must have
• Firm name :BELLWOOD & TRASK
Business Consultants & Accountants
Address: Level 2 Units 3 & 4, 17 Merrow Crescent DALEFORD SA 5099
Box address: PO Box 418 ASHGROVE SA 5098
telp: +61 8 8555 0142
fax: +61 8 8555 0187

Martin Bellwood, CA
Lucas Trask, CPA

martin.bellwood@bellwoodtrask.example.com.au
lucas.trask@bellwoodtrask.example.com.au

Dark Navy Blue as primary colour

```html
<!DOCTYPE html>
<html lang="en">
<head>
<meta charset="utf-8">
<title>Bellwood &amp; Trask – Business Card</title>
<link rel="stylesheet" href="https://fonts.googleapis.com/css2?family=Arimo:wght@400;700&family=Source+Sans+3:wght@400;600&display=swap">
<style>
  :root {
    --navy: #0a0a9a;
    --backdrop: #2a2a2a;
    --card-light: #f4f4f4;
    --card-mid: #d2d2d2;
    --ink: #111111;
    --ink-soft: #555555;
    --ghost: rgba(255, 255, 255, 0.38);
    --white: #ffffff;
  }
  * { box-sizing: border-box; margin: 0; padding: 0; }
  html, body { width: 900px; height: 1200px; overflow: hidden; }
  body { background: var(--backdrop); position: relative; font-family: "Arimo", Arial, sans-serif; }

  .card { position: absolute; width: 656px; height: 376px; overflow: hidden; }

  /* Front */
  .card-front {
    left: 114px; top: 138px;
    background: radial-gradient(ellipse 60% 70% at 36% 32%, var(--card-light) 0%, #e2e2e2 45%, var(--card-mid) 100%);
  }
  .accent-top { position: absolute; right: 0; top: 0; width: 382px; height: 18px; background: var(--navy); }
  .accent-side { position: absolute; left: 0; bottom: 0; width: 15px; height: 100px; background: var(--navy); }
  .ghost-name {
    position: absolute; left: 40px; top: 42px;
    font-weight: 700; font-size: 150px; letter-spacing: -2px;
    color: var(--ghost); white-space: nowrap; line-height: 1;
  }
  .identity { position: absolute; left: 62px; top: 96px; }
  .holder-name { font-weight: 700; color: var(--ink); white-space: nowrap; line-height: 1; letter-spacing: -0.5px; }
  .holder-name .first { font-size: 48px; }
  .holder-name .last { font-size: 33px; margin-left: 4px; }
  .holder-role { margin-top: 12px; text-align: right; font-size: 16.5px; color: var(--ink-soft); }

  .contact {
    position: absolute; right: 14px; top: 289px;
    display: grid; grid-template-columns: auto auto auto; column-gap: 6px; row-gap: 2px;
    font-size: 12.5px; line-height: 16.5px;
  }
  .contact dt { color: var(--white); text-align: right; }
  .contact .dot { color: var(--ink-soft); font-size: 9px; }
  .contact dd { color: var(--ink-soft); }

  /* Back */
  .card-back { left: 132px; top: 722px; height: 386px; background: var(--navy); color: var(--white); font-family: "Source Sans 3", "Myriad Pro", sans-serif; text-align: center; }
  .firm { position: absolute; left: 0; right: 0; top: 112px; transform: translateX(-187px); left: 50%; width: 374px; margin-left: 0; }
  .firm-name { font-weight: 600; font-size: 27px; letter-spacing: 0.2px; line-height: 1; }
  .firm-tagline { font-size: 17px; margin-top: 6px; }
  .firm-address { margin-top: 22px; font-size: 14px; line-height: 23px; }
</style>
</head>
<body>
  <section class="card card-front" aria-label="Business card front">
    <div class="accent-top"></div>
    <div class="accent-side"></div>
    <div class="ghost-name" aria-hidden="true">Martin</div>
    <div class="identity">
      <h1 class="holder-name"><span class="first">Martin</span><span class="last">Bellwood</span></h1>
      <p class="holder-role">Business consultant</p>
    </div>
    <dl class="contact">
      <dt>Phone</dt><span class="dot">●</span><dd>+61 8 8555 0142</dd>
      <dt>Fax</dt><span class="dot">●</span><dd>+61 8 8555 0187</dd>
      <dt>Email</dt><span class="dot">●</span><dd>martin@bellwoodtrask.example.com</dd>
      <dt>Web</dt><span class="dot">●</span><dd>www.bellwoodtrask.example.com.au</dd>
    </dl>
  </section>

  <section class="card card-back" aria-label="Business card back">
    <div class="firm">
      <h2 class="firm-name">BELLWOOD &amp; TRASK</h2>
      <p class="firm-tagline">Business Consultants &amp; Accountants</p>
      <address class="firm-address" style="font-style:normal">
        PO Box 418 ASHGROVE SA 5098<br>
        Level 2 Units 3 &amp; 4, 17 Merrow Crescent<br>
        DALEFORD SA 5099
      </address>
    </div>
  </section>
</body>
</html>
```